Pagecraft Design Project - Vibrant Children's school bag website

We need a fresh design for the landing page of our new web site and blog: quillonmarket.com

Tamborine specialises in supplying schools all over the world and now also parents directly with, personalised school bags, accessories, crafts and gifts for their children.

I have attached the visual that our web designers have provided so that we can see the layout of the various window, but now we need to add the personal touch of making it our own and visually making the site look enticing and exciting to shop on.
Updates

Hello Designers,

We are now in the final round of choosing a design.  We have found that most deisgns are very similar and that none are completley original.  Therefore, we are willing to throw our wire frame away and start with a compleltely new visual so you can design what ever you like!

The only requirements we have is that we must have:
- A large rolling banner to show our products lines
- Our Company logo
- Meta going tags across the top
- Icons for chatterbook,snipboard,blog,
- Account Login bar
- A log in area for schools
- A login area to register for the Club Tambo

So we are looking for something that really stands out from the crowd!

can you deliver?

Thanks,

Target Market(s)

To appeal to mum's shopping on line for their children's school items and gifts.

Industry/Entity Type

School

Requirements
Must have
• -When you see the visual attached please note the amendments:
- the word 'school bags' under our company name will not appear
- the tag line "Australia's no 1 specialist school bag company' should be deleted. We will leave this area open so that you can include some simple icons that we would like featured across the top of the banner i.e:
- a love heart icon + wording to say : Made with love
- A 'delivery' icon + wording to say : Free delivery
- A 'warranty' icon + wording to say : up to 25 year warranty
- A 'world' icon + wording to say : we ship to the universe
(Please see: www.pebblecrate.com.au for reference of what we mean!)

We we want the overall design to be clean, fresh, crisp and fun to look at.

You may alter the colours of everything, even the coloured tabs. we think that the coloured tabs should actually just be one colour through out and to let the tamborine name stand out with all it's.

The top/main photo will be a rolling banner.

You can change the shapes of the boxes but keep to the wire frame.

Please alter the design of the black/coloured club tambo card to suit your design.

Our aim is to also change the side panels in peak seasons to reflect halloween banner, christmas banner etc.

Please see my screen shot of the current page and see where the "dots' pattern sits on either side of the shopping panels. Please include the side panels as we want to change the design to have themes i.e for halloween, for christmas etc etc.

example of websites that have this:

http://www.wavemoorly.com/

Please include a 'blog' and snipboard icon.

The site will not only manage our retail sales but will also be a portal for our schools to register and place their bulk orders with us. So the "wholesale register box" must stand out so our school customers can easily see where they need to click & register.
Should not have
• Please do not do a 'baby' boutique theme. We need a theme that appeals to mum's that have children across the ages of 3-14 years.

```html
<!DOCTYPE html>
<html lang="en">
<head>
<meta charset="utf-8">
<title>Tamborine – School Bags, Accessories, Crafts and Gifts</title>
<link href="https://fonts.googleapis.com/css2?family=Bree+Serif&family=Open+Sans:wght@400;600;700&display=swap" rel="stylesheet">
<style>
:root{
  --ink:#222;
  --muted:#555;
  --topbar:#1a1a1a;
  --red:#d9141b;
  --red-dark:#b00d12;
  --yellow:#f7b21c;
  --yellow-deep:#ef9c10;
  --green:#7dbd1e;
  --green-dark:#5f9a10;
  --slate:#5a5a5a;
  --slate-dark:#3f3f3f;
  --panel:#eeeeee;
  --card:#ffffff;
  --line:#d6d6d6;
  --orange:#ee7322;
  --footer:#444444;
  --footer-base:#333333;
  --price:#e21b1b;
  --logo:#e8361f;
}
*{box-sizing:border-box;margin:0;padding:0}
html,body{width:1200px;height:2249px;overflow:hidden;background:#fff}
body{font-family:"Open Sans",Arial,sans-serif;color:var(--ink);position:relative}
.abs{position:absolute}

/* top bar */
.topbar{left:0;top:0;width:1200px;height:25px;background:var(--topbar);color:#fff;font-size:14px}
.topbar .phone{left:140px;top:3px;display:flex;align-items:center;gap:8px;font-weight:600}
.topbar .account{left:945px;top:3px;display:flex;align-items:center;gap:6px}

/* header */
.header{left:0;top:25px;width:1200px;height:150px;background:linear-gradient(#fff 55%,#ececec)}
.logo{left:150px;top:28px;font-family:"Bree Serif",Georgia,serif;font-size:62px;color:var(--logo);line-height:1}
.perks{left:505px;top:15px;display:flex;gap:22px}
.perk{display:flex;align-items:center;gap:10px;font-family:"Bree Serif",Georgia,serif;font-size:14px;line-height:1.2;color:#555;text-align:center}
.perk + .perk{border-left:1px solid #ddd;padding-left:20px}
.bag{left:622px;top:92px;width:241px;height:42px;border:1px solid #ccc;background:#fff;font-size:10px;padding:4px 0 0 20px;color:#333}
.bag b{font-family:"Bree Serif",Georgia,serif;font-weight:400;color:var(--red);font-size:13px}
.bag .tote{position:absolute;right:14px;top:-6px}
.search{left:886px;top:97px;width:163px;height:32px;background:#fff;border:1px solid #ddd;box-shadow:0 1px 3px rgba(0,0,0,.15);font-size:10px;color:#999;padding:9px 0 0 10px}
.search svg{position:absolute;right:10px;top:8px}

/* nav */
.nav{left:0;top:175px;width:1200px;height:38px;background:linear-gradient(var(--red),var(--red-dark));display:flex;align-items:center;padding-left:150px;gap:27px}
.nav a{color:#fff;text-decoration:none;font-size:13px;font-weight:600}

/* banner */
.banner{left:0;top:213px;width:1200px;height:403px;background:radial-gradient(ellipse at 50% 45%,#fcc838,var(--yellow) 55%,var(--yellow-deep))}
.banner h1{left:150px;top:80px;width:420px;font-family:"Bree Serif",Georgia,serif;font-weight:400;font-size:27px;line-height:1.3;color:#fff}
.shop-now{left:228px;top:260px;width:156px;height:49px;border-radius:6px;background:linear-gradient(#ee2a2a,#b40c0c);color:#fff;font-family:"Bree Serif",Georgia,serif;font-size:24px;display:flex;align-items:center;justify-content:center;gap:8px;box-shadow:0 3px 6px rgba(0,0,0,.25)}
.banner-visual{left:524px;top:28px;width:508px;height:324px;border-radius:30px;background:radial-gradient(ellipse at 50% 55%,#7a6fa2,#c6a059 60%,rgba(247,178,28,0) 75%)}
.dots{left:553px;top:381px;display:flex;gap:4px}
.dots i{width:16px;height:16px;border-radius:50%;background:#6b3d06;display:block}
.dots i.on{background:#e35a06}

/* product panel */
.panel{left:140px;top:640px;width:620px;height:1253px;background:var(--panel);border:1px solid #e2e2e2}
.sec-head{left:132px;width:628px;height:34px;display:flex;align-items:center;justify-content:space-between;padding:0 14px 0 16px}
.sec-head h2{font-family:"Bree Serif",Georgia,serif;font-weight:400;font-size:22px;color:#fff}
.sec-head .view{background:#2d2d2d;color:#fff;font-size:12px;border-radius:12px;padding:3px 16px}
.sec-head.green{background:linear-gradient(#8fcc26,var(--green-dark))}
.sec-head.slate{background:linear-gradient(var(--slate),var(--slate-dark))}
.sec-head::after{content:"";position:absolute;left:0;bottom:-8px;border-left:8px solid transparent;border-top:8px solid #222}
.card{width:179px;height:226px;background:var(--card);box-shadow:0 0 6px rgba(0,0,0,.12)}
.card .photo{position:absolute;left:14px;top:12px;width:151px;height:130px;border:1px solid var(--line)}
.card .name{position:absolute;left:14px;top:150px;font-size:12px}
.card .price{position:absolute;right:14px;top:150px;font-size:13px;color:var(--price)}
.card .buy{position:absolute;left:14px;top:187px;width:86px;height:26px;border-radius:4px;background:linear-gradient(#8fcc26,var(--green-dark));color:#fff;font-size:12px;font-weight:700;display:flex;align-items:center;justify-content:center}

/* sidebar */
.side-title{font-family:"Bree Serif",Georgia,serif;font-size:18px;line-height:1.3;color:#333}
.field{width:254px;height:30px;border:2px solid #d8d8d8;border-radius:3px;background:#fff;font-size:10px;color:#999;font-style:italic;padding:7px 0 0 8px}
.btn-dark{height:32px;border-radius:5px;background:linear-gradient(#4a4a4a,#1e1e1e);color:#fff;font-size:14px;font-weight:700;display:flex;align-items:center;justify-content:center}
.btn-hot{height:32px;border-radius:5px;background:linear-gradient(#ffc21a,#f25a0a);color:#fff;font-size:14px;font-weight:700;display:flex;align-items:center;justify-content:center}
.rule{width:254px;height:1px;background:#e2e2e2}
.club-card{left:968px;top:880px;width:102px;height:66px;border-radius:8px;transform:rotate(-14deg);background:linear-gradient(135deg,#222,#333 40%,#c23a8f 55%,#f4c012 70%,#3aa0db)}
.news-title{font-family:"Bree Serif",Georgia,serif;font-size:18px;color:var(--red)}
.news{width:254px;height:74px;border-bottom:1px solid #e2e2e2}
.news .day{position:absolute;left:6px;top:4px;font-family:"Bree Serif",Georgia,serif;font-size:27px;color:var(--red);line-height:1}
.news .mon{position:absolute;left:2px;top:34px;font-size:13px;color:#333}
.news p{position:absolute;left:50px;top:4px;font-size:11px;line-height:1.6;color:#333}
.news .more{color:var(--red);font-style:italic;font-size:10px}
.view-all{left:805px;top:1413px;width:266px;height:30px;background:#e6e6e6;font-size:11px;color:#666;display:flex;align-items:center;justify-content:center}
.community{left:805px;top:1460px;width:266px;height:173px;border:4px solid var(--orange);background:var(--orange)}
.community h3{font-family:"Bree Serif",Georgia,serif;font-weight:400;color:#fff;font-size:18px;padding:3px 0 0 10px;height:36px}
.community .partner{background:#eef3f7;height:125px;display:flex;flex-direction:column;align-items:center;justify-content:center;gap:4px;font-family:"Bree Serif",Georgia,serif;color:#2e7a3a;font-size:22px}
.community .partner small{font-family:"Open Sans",Arial,sans-serif;font-size:9px;color:#c0301c}
.promo{left:805px;top:1658px;width:266px;height:175px;border:1px solid #ccc;background:radial-gradient(circle at 50% 40%,#7fce3c,#2f8f1e 70%,#1f6e14)}
.promo span{position:absolute;left:0;right:0;top:14px;text-align:center;font-family:"Bree Serif",Georgia,serif;font-size:22px;color:#fff}

/* footer */
.footer{left:0;top:1960px;width:1200px;height:254px;background:var(--footer);color:#ddd}
.footer h4{font-family:"Bree Serif",Georgia,serif;font-weight:400;font-size:18px;color:#fff}
.footer ul{list-style:none;font-size:12px;line-height:23.5px;margin-top:8px}
.footer .col{top:30px}
.footer .divider{top:30px;width:1px;height:195px;background:#555}
.social li{display:flex;align-items:center;gap:8px}
.social i{width:13px;height:13px;border-radius:2px;display:block}
.base{left:0;top:2214px;width:1200px;height:35px;background:var(--footer-base);color:#ccc;font-size:12px;text-align:center;line-height:35px}
</style>
</head>
<body>

<div class="abs topbar">
  <div class="abs phone">
    <svg width="14" height="14" viewBox="0 0 24 24"><path fill="#fff" d="M6.6 10.8a15 15 0 0 0 6.6 6.6l2.2-2.2c.3-.3.7-.4 1-.2 1.1.4 2.3.6 3.6.6.6 0 1 .4 1 1V20c0 .6-.4 1-1 1A17 17 0 0 1 3 4c0-.6.4-1 1-1h3.5c.6 0 1 .4 1 1 0 1.3.2 2.5.6 3.6.1.3 0 .7-.2 1z"/></svg>
    +22 555 014 207
  </div>
  <div class="abs account">Account Login
    <svg width="13" height="13" viewBox="0 0 14 14"><circle cx="7" cy="7" r="6" fill="none" stroke="#fff" stroke-width="1.4"/><path d="M6 4l3 3-3 3" fill="none" stroke="#fff" stroke-width="1.4"/></svg>
  </div>
</div>

<header class="abs header">
  <div class="abs logo">tamborine</div>
  <div class="abs perks">
    <div class="perk">
      <svg width="34" height="30" viewBox="0 0 24 22"><path fill="#e0261f" d="M12 21 2.5 11.5A5.5 5.5 0 0 1 12 4a5.5 5.5 0 0 1 9.5 7.5z"/></svg>
      <span>Made<br>with love</span>
    </div>
    <div class="perk">
      <svg width="46" height="30" viewBox="0 0 46 30"><rect x="1" y="4" width="28" height="18" fill="#d62a20"/><path d="M29 10h9l6 6v6H29z" fill="#b51d15"/><rect x="32" y="12" width="6" height="4" fill="#fff"/><circle cx="9" cy="24" r="4" fill="#333"/><circle cx="37" cy="24" r="4" fill="#333"/></svg>
      <span>Free<br>delivery</span>
    </div>
    <div class="perk">
      <svg width="32" height="32" viewBox="0 0 32 32"><circle cx="16" cy="16" r="14" fill="#8a6b3b"/><circle cx="16" cy="16" r="9" fill="#c9a461"/><circle cx="16" cy="16" r="4" fill="#5b4422"/></svg>
      <span>up to 25<br>year warranty</span>
    </div>
    <div class="perk">
      <svg width="30" height="30" viewBox="0 0 30 30"><circle cx="15" cy="15" r="13" fill="#2b8ad6"/><path d="M8 9c3-1 5 1 6 3s-1 4 1 6-2 5-4 4-2-4-4-5-2-6 1-8zm12 2c2 0 4 2 3 5s-3 3-4 1 0-6 1-6z" fill="#4fae3a"/></svg>
      <span>we ship to<br>the universe</span>
    </div>
  </div>
  <div class="abs bag">
    <b>Shopping Bag</b> (0 items)<br>Spend N-25, Get FREE SHIPPING
    <svg class="tote" width="36" height="44" viewBox="0 0 36 44"><path d="M10 12a8 8 0 0 1 16 0" fill="none" stroke="#1f6fb0" stroke-width="2"/><rect x="3" y="12" width="30" height="30" fill="#2a8ad4"/></svg>
  </div>
  <div class="abs search">Search for Products
    <svg width="16" height="16" viewBox="0 0 16 16"><circle cx="6.5" cy="6.5" r="5" fill="none" stroke="#222" stroke-width="2"/><path d="M10 10l5 5" stroke="#222" stroke-width="2.4"/></svg>
  </div>
</header>

<nav class="abs nav">
  <a>Test Menu</a><a>Kids Backpacks</a><a>Kids Bags</a><a>Sports</a><a>Kids Clothing</a><a>Art &amp; Craft</a><a>Music</a><a>Kids Diaries</a><a>Kids Storage</a><a>Extra Stuff</a><a>Sale</a>
</nav>

<section class="abs banner">
  <h1 class="abs">Neque porro quisquam est qui dolorem ipsum quia dolor amet, consectetur, adipisci velit...</h1>
  <div class="abs shop-now">Shop Now
    <svg width="14" height="14" viewBox="0 0 14 14"><circle cx="7" cy="7" r="6" fill="none" stroke="#fff" stroke-width="1.4"/><path d="M6 4l3 3-3 3" fill="none" stroke="#fff" stroke-width="1.4"/></svg>
  </div>
  <div class="abs banner-visual" role="img" aria-label="Product photo: school stationery, ring binders, notebooks, a cap and a calculator"></div>
  <div class="abs dots"><i class="on"></i><i></i><i></i><i></i><i></i></div>
</section>

<div class="abs panel"></div>

<!-- Featured Products -->
<div class="abs sec-head green" style="top:659px"><h2>Featured Products</h2><span class="view">View All</span></div>
<div class="abs card" style="left:164px;top:716px"><div class="photo" role="img" aria-label="Red school backpack" style="background:radial-gradient(circle,#d8343c,#f3f3f3 70%)"></div><span class="name">School Bags</span><span class="price">$88.00</span><span class="buy">Shop Now!</span></div>
<div class="abs card" style="left:360px;top:716px"><div class="photo" role="img" aria-label="Stationery set with pencils and notebooks" style="background:radial-gradient(circle,#6a8fc4,#f3f3f3 70%)"></div><span class="name">Accessories</span><span class="price">$88.00</span><span class="buy">Shop Now!</span></div>
<div class="abs card" style="left:556px;top:716px"><div class="photo" role="img" aria-label="White plush toy" style="background:radial-gradient(circle,#e6e0d2,#f7f7f7 70%)"></div><span class="name">Crafts and Gifts</span><span class="price">$88.00</span><span class="buy">Shop Now!</span></div>

<!-- School Bags -->
<div class="abs sec-head slate" style="top:970px"><h2>School Bags</h2><span class="view">View All</span></div>
<div class="abs card" style="left:164px;top:1027px"><div class="photo" role="img" aria-label="Grey backpack" style="background:radial-gradient(circle,#6d7470,#f3f3f3 70%)"></div><span class="name">Lorem Ipsum...</span><span class="price">$88.00</span><span class="buy">Shop Now!</span></div>
<div class="abs card" style="left:360px;top:1027px"><div class="photo" role="img" aria-label="Orange backpack" style="background:radial-gradient(circle,#e67a22,#f3f3f3 70%)"></div><span class="name">Lorem Ipsum...</span><span class="price">$88.00</span><span class="buy">Shop Now!</span></div>
<div class="abs card" style="left:556px;top:1027px"><div class="photo" role="img" aria-label="Checked brown backpack" style="background:radial-gradient(circle,#8a6a55,#f3f3f3 70%)"></div><span class="name">Lorem Ipsum...</span><span class="price">$88.00</span><span class="buy">Shop Now!</span></div>

<!-- Accessories -->
<div class="abs sec-head slate" style="top:1281px"><h2>Accessories</h2><span class="view">View All</span></div>
<div class="abs card" style="left:164px;top:1338px"><div class="photo" role="img" aria-label="Coloured pencils in a cup" style="background:radial-gradient(circle,#e0a93a,#f3f3f3 70%)"></div><span class="name">Lorem Ipsum...</span><span class="price">$88.00</span><span class="buy">Shop Now!</span></div>
<div class="abs card" style="left:360px;top:1338px"><div class="photo" role="img" aria-label="Alarm clock with school books" style="background:radial-gradient(circle,#7c7f86,#f3f3f3 70%)"></div><span class="name">Lorem Ipsum...</span><span class="price">$88.00</span><span class="buy">Shop Now!</span></div>
<div class="abs card" style="left:556px;top:1338px"><div class="photo" role="img" aria-label="Desk globe" style="background:radial-gradient(circle,#3f8fd0,#f3f3f3 70%)"></div><span class="name">Lorem Ipsum...</span><span class="price">$88.00</span><span class="buy">Shop Now!</span></div>

<!-- Crafts and Gifts -->
<div class="abs sec-head slate" style="top:1592px"><h2>Crafts and Gifts</h2><span class="view">View All</span></div>
<div class="abs card" style="left:164px;top:1649px"><div class="photo" role="img" aria-label="Gift box full of toys" style="background:radial-gradient(circle,#c8282c,#f3f3f3 70%)"></div><span class="name">Lorem Ipsum...</span><span class="price">$88.00</span><span class="buy">Shop Now!</span></div>
<div class="abs card" style="left:360px;top:1649px"><div class="photo" role="img" aria-label="Silver gift box with gold ribbon" style="background:radial-gradient(circle,#c9c9c9,#f3f3f3 70%)"></div><span class="name">Lorem Ipsum...</span><span class="price">$88.00</span><span class="buy">Shop Now!</span></div>
<div class="abs card" style="left:556px;top:1649px"><div class="photo" role="img" aria-label="Wooden hand drum" style="background:radial-gradient(circle,#9a3a1e,#f3f3f3 70%)"></div><span class="name">Lorem Ipsum...</span><span class="price">$88.00</span><span class="buy">Shop Now!</span></div>

<!-- Sidebar -->
<div class="abs side-title" style="left:805px;top:652px">School &amp; Reseller<br>Registration</div>
<div class="abs field" style="left:805px;top:710px">Enter Your User Name :</div>
<div class="abs field" style="left:805px;top:757px">Enter Your Password :</div>
<div class="abs btn-dark" style="left:805px;top:804px;width:74px">Login</div>
<div class="abs btn-hot" style="left:890px;top:804px;width:122px">Register Now!</div>
<div class="abs rule" style="left:805px;top:856px"></div>

<div class="abs side-title" style="left:805px;top:872px">Club Tambo</div>
<div class="abs" style="left:805px;top:906px;font-size:12px;line-height:1.55">Join now for 15% off your<br>first order*</div>
<div class="abs club-card" role="img" aria-label="Club Tambo membership card"></div>
<div class="abs field" style="left:805px;top:955px">Enter Your Email Address :</div>
<div class="abs btn-dark" style="left:805px;top:1000px;width:87px">join Now!</div>
<div class="abs rule" style="left:805px;top:1052px"></div>

<div class="abs news-title" style="left:805px;top:1070px">News &amp; Blog</div>
<div class="abs news" style="left:805px;top:1110px"><span class="day">19</span><span class="mon">JUN</span><p>Lorem Ipsum is simply dummy text<br>Lorem Ipsum&nbsp; the industry's...<br><span class="more">Read More...</span></p></div>
<div class="abs news" style="left:805px;top:1188px"><span class="day">19</span><span class="mon">JUN</span><p>Lorem Ipsum is simply dummy text<br>Lorem Ipsum&nbsp; the industry's...<br><span class="more">Read More...</span></p></div>
<div class="abs news" style="left:805px;top:1265px"><span class="day">19</span><span class="mon">JUN</span><p>Lorem Ipsum is simply dummy text<br>Lorem Ipsum&nbsp; the industry's...<br><span class="more">Read More...</span></p></div>
<div class="abs news" style="left:805px;top:1342px;border-bottom:none"><span class="day">19</span><span class="mon">JUN</span><p>Lorem Ipsum is simply dummy text<br>Lorem Ipsum&nbsp; the industry's...<br><span class="more">Read More...</span></p></div>
<div class="abs view-all">View All</div>

<div class="abs community">
  <h3>Community</h3>
  <div class="partner">Kindhaven<small>Helping every child thrive</small></div>
</div>

<div class="abs promo" role="img" aria-label="Weekly discounts Christmas banner with gifts and a buy now ribbon"><span>WEEKLY DISCOUNTS</span></div>

<footer class="abs footer">
  <div class="abs col" style="left:188px"><h4>Quick Links</h4>
    <ul><li>Test Menu</li><li>Kids Backpacks</li><li>Kids Bags</li><li>Sports</li><li>Kids Clothing</li><li>Art &amp; Craft</li></ul></div>
  <div class="abs divider" style="left:348px"></div>
  <div class="abs col" style="left:405px;top:53px"><ul><li>Music</li><li>Kids Diaries</li><li>Kids Storage</li><li>Extra Stuff</li><li>Sale</li></ul></div>
  <div class="abs divider" style="left:558px"></div>
  <div class="abs col" style="left:610px"><h4>Featured products</h4>
    <ul><li>School Bags</li><li>Accessories</li><li>Craft and Gifts</li></ul></div>
  <div class="abs divider" style="left:812px"></div>
  <div class="abs col" style="left:863px"><h4>Connect With Us</h4>
    <ul class="social"><li><i style="background:#ee7a1c"></i>Blog</li><li><i style="background:#cf2027"></i>Snipboard</li></ul></div>
</footer>
<div class="abs base">Copyright © 2012 Tamborine.All Rights Reserved.</div>

</body>
</html>
```